An international wholesale business needs letterhead design

Logo file is attached. Please design a letterhead with the following details:

- Company Name and Logo
- Address
- VAT Registration number
- Phone No
- Website address

```html
<!DOCTYPE html>
<html lang="en">
<head>
<meta charset="UTF-8">
<title>Korvel Trading Letterhead</title>
<link href="https://fonts.googleapis.com/css2?family=Poppins:wght@400;600&display=swap" rel="stylesheet">
<style>
  :root {
    --backdrop: #eceeef;
    --paper: #ffffff;
    --brand-red: #c1272d;
    --charcoal: #231f20;
    --charcoal-light: #454545;
    --steel: #8b9298;
    --text-light: #ffffff;
  }
  html, body {
    margin: 0;
    width: 1200px;
    height: 1200px;
    overflow: hidden;
    background: var(--backdrop);
  }
  .canvas {
    width: 1200px;
    height: 1200px;
    display: flex;
    align-items: center;
    justify-content: center;
  }
  .letterhead {
    width: 791px;
    height: 1119px;
    display: block;
  }
  .sheet { fill: var(--paper); }
  .band-red { fill: var(--brand-red); }
  .band-steel { fill: var(--steel); }
  .contact-text, .footer-text {
    font-family: 'Poppins', sans-serif;
    font-weight: 400;
    fill: var(--text-light);
  }
  .contact-text { font-size: 23px; }
  .footer-text { font-size: 24px; }
  .brand-name {
    font-family: 'Poppins', sans-serif;
    font-weight: 600;
    font-size: 34px;
    letter-spacing: 1px;
    fill: var(--brand-red);
  }
  .brand-dot { fill: var(--brand-red); }
  .icon-fill { fill: var(--brand-red); }
  .icon-line { fill: none; stroke: var(--brand-red); stroke-width: 2; }
</style>
</head>
<body>
<main class="canvas">
  <svg class="letterhead" viewBox="438 220 1055 1492" xmlns="http://www.w3.org/2000/svg" aria-label="Korvel Trading letterhead">
    <defs>
      <radialGradient id="header-shade" cx="0.5" cy="0.5" r="0.5" gradientUnits="objectBoundingBox" gradientTransform="translate(0 0) scale(1 1)">
        <stop offset="0" stop-color="var(--charcoal-light)"/>
        <stop offset="1" stop-color="var(--charcoal)"/>
      </radialGradient>
      <linearGradient id="bar-shade-header" x1="438" x2="1493" y1="0" y2="0" gradientUnits="userSpaceOnUse">
        <stop offset="0" stop-color="#231f20"/>
        <stop offset="0.5" stop-color="#454545"/>
        <stop offset="1" stop-color="#231f20"/>
      </linearGradient>
      <linearGradient id="bar-shade-footer" x1="438" x2="1493" y1="0" y2="0" gradientUnits="userSpaceOnUse">
        <stop offset="0.25" stop-color="#231f20"/>
        <stop offset="0.55" stop-color="#454545"/>
        <stop offset="0.95" stop-color="#231f20"/>
      </linearGradient>
    </defs>

    <rect class="sheet" x="438" y="220" width="1055" height="1492"/>

    <!-- Header -->
    <g class="header">
      <polygon class="band-red" points="438,284 966,284 992,332 438,332"/>
      <rect x="438" y="332" width="1055" height="146" fill="url(#bar-shade-header)"/>
      <polygon class="band-red" points="1012,478 1493,478 1493,525 1037,525"/>
      <polygon class="band-steel" points="966,284 1028,284 1157,525 1097,525"/>

      <g class="brand">
        <circle class="brand-dot" cx="592" cy="404" r="14"/>
        <text class="brand-name" x="620" y="416">KORVEL TRADING</text>
      </g>

      <g class="contacts">
        <path class="icon-fill" d="M1167 357c2-2 5-2 6 0l3 4c1 2 1 4-1 5l-2 2c1 3 4 6 7 8l2-2c1-2 3-2 5-1l4 3c2 1 2 4 0 6l-2 2c-3 3-10 0-16-6s-9-13-6-16z"/>
        <text class="contact-text" x="1206" y="376">+0123 456 7890</text>

        <g class="icon-line">
          <circle cx="1176" cy="408" r="12"/>
          <ellipse cx="1176" cy="408" rx="5" ry="12"/>
          <line x1="1164" y1="408" x2="1188" y2="408"/>
          <line x1="1166" y1="401" x2="1186" y2="401"/>
          <line x1="1166" y1="415" x2="1186" y2="415"/>
        </g>
        <text class="contact-text" x="1206" y="416">www.website.com</text>

        <path class="icon-fill" d="M1176 437c-6 0-10 4-10 10 0 7 10 15 10 15s10-8 10-15c0-6-4-10-10-10zm0 14a4 4 0 1 1 0-8 4 4 0 0 1 0 8z"/>
        <text class="contact-text" x="1206" y="456">Company Address</text>
      </g>
    </g>

    <!-- Footer -->
    <g class="footer">
      <polygon class="band-red" points="918,1509 1493,1509 1493,1557 892,1557"/>
      <rect x="438" y="1557" width="1055" height="60" fill="url(#bar-shade-footer)"/>
      <polygon class="band-red" points="438,1617 920,1617 895,1663 438,1663"/>
      <polygon class="band-steel" points="857,1509 918,1509 835,1663 775,1663"/>
      <text class="footer-text" x="973" y="1595">VAT Registration no:</text>
    </g>
  </svg>
</main>
</body>
</html>
```